QM - menu design

Hi,

We require elegant menu design for upscale restaurant. Please find attached the logo and the menu items for your reference.

for inspiration, this is a good website: -
http://www.plivermark.com/tablefolio/about.php

We are very much open for Menu Size suggestions.

unfortunately the place is going under renovation, we don't have updated images to it. the closest look and feel to our place is http://vessora.com ..

we are also open for creative options on the shape, the styles, etc. as long as it represents the fine dine feel ...

Thanks ...
Updates

Dear All,

We wouldlike to extend our apology for not being able to provide feedbacks on everysingle design. We were extremely busy and we have multiple contests opensimultaneously which makes the process even harder.

However,we would like to thank you all for the efforts you have put into designingour menu. It is very much appreciated …

We wishyou all success in your design ventures and we are quite positive that we willbe working with many of you on many projects in the soon future. 

Thanks & Regards,

DHI Team...

 

 

 

Industry/Entity Type

Restaurant

Requirements
Must have
• Please ensure that there are 'some' images in the menu ... this is very important.
Should not have
• IMPORTANT: -

1. Please DO NOT insert any currency sign to the menu
2. Please keep the prices of the menu at the end of the menu items descriptions NOT beside the menu item names. The font of the price should be similar to the menu item description and please DO NOT bold the numbers. the prices should be subtle.

Thank you ...

```html
<!DOCTYPE html>
<html lang="en">
<head>
<meta charset="utf-8">
<title>Quaymore Cafe – Menu Spread</title>
<link rel="stylesheet" href="https://fonts.googleapis.com/css2?family=Encode+Sans+Condensed:wght@300;400&family=Roboto+Condensed:wght@300;400&display=swap">
<style>
  :root{
    --paper:#ffffff;
    --wine:#2b0c17;
    --wine-edge:#4a2232;
    --title:#e9cfd6;
    --item:#dcbcc5;
    --desc:#a98591;
    --hole:#f3eef0;
    --accent:#c98aa0;
  }
  *{margin:0;padding:0;box-sizing:border-box}
  html,body{width:1200px;height:561px;overflow:hidden;background:var(--paper)}
  .spread{position:relative;width:1200px;height:561px}
  .page{position:absolute;height:263px;background:var(--wine);border-radius:9px;padding:12px 9px 8px;color:var(--item)}
  .row-top{top:0}
  .row-bottom{top:288px}
  .tab{position:absolute;top:36px;width:16px;height:204px;background:var(--wine)}
  .tab-left .tab{left:-15px;border-radius:8px 0 0 8px}
  .tab-right .tab{right:-15px;border-radius:0 8px 8px 0}
  .tab::before,.tab::after{content:"";position:absolute;width:7px;height:7px;border-radius:50%;background:var(--hole);left:5px}
  .tab::before{top:58px}
  .tab::after{top:134px}
  .page::before{content:"";position:absolute;top:30px;bottom:30px;border-left:1px dashed var(--wine-edge)}
  .tab-left::before{left:3px}
  .tab-right::before{right:3px}
  .page-title{font-family:"Encode Sans Condensed",sans-serif;font-weight:300;font-size:11.5px;color:var(--title);text-align:center;line-height:1.1;margin-bottom:14px}
  .page-title small{display:block;font-size:8.5px;margin-top:2px}
  .items{font-family:"Roboto Condensed",sans-serif;font-weight:300;font-size:3.4px;line-height:1.35;padding:0 4px}
  .item{margin-bottom:5px;overflow:hidden}
  .item b{display:block;font-weight:400;font-size:3.8px;color:var(--item)}
  .item span{color:var(--desc)}
  .price{float:right;color:var(--desc);padding-left:3px}
  .compact .item{margin-bottom:3.6px}
  .list .item{margin-bottom:2.6px;color:var(--item)}
  .subhead{font-family:"Encode Sans Condensed",sans-serif;font-size:4.4px;color:var(--title);margin:5px 0 3px}
  .rule{border-top:1px solid var(--wine-edge);margin:6px 0}
  .cover{display:flex;flex-direction:column;align-items:center;text-align:center}
  .brand{margin-top:98px;font-family:"Encode Sans Condensed",sans-serif;font-weight:300;font-size:13px;letter-spacing:2.5px;color:var(--title)}
  .brand-sub{font-family:"Encode Sans Condensed",sans-serif;font-size:4px;letter-spacing:2px;color:var(--title);margin-top:2px}
  .cover-menu{margin-top:92px;font-family:"Encode Sans Condensed",sans-serif;font-weight:300;font-size:11px;color:var(--title)}
  .cover-tagline{font-family:"Encode Sans Condensed",sans-serif;font-size:5px;color:var(--accent);margin-top:2px;word-spacing:2px}
</style>
</head>
<body>
<main class="spread">

  <section class="page row-top tab-left cover" style="left:162px;width:102px">
    <div class="tab"></div>
    <div class="brand">QUAYMORE</div>
    <div class="brand-sub">CAFE</div>
    <div class="cover-menu">MENU</div>
    <div class="cover-tagline">Dishes Drinks Desserts</div>
  </section>

  <section class="page row-top tab-left" style="left:294px;width:102px"><div class="tab"></div></section>

  <section class="page row-top tab-left" style="left:452px;width:106px">
    <div class="tab"></div>
    <h2 class="page-title">Breakfast</h2>
    <div class="items">
      <p class="item"><b>Butter Croissant</b><span>Freshly baked flaky croissant served warm with salted butter and a choice of apricot or strawberry jam</span> <span class="price">18</span></p>
      <p class="item"><b>Cheese Croissant</b><span>Golden croissant filled with melted cheddar and served with a small green side salad</span> <span class="price">22</span></p>
      <p class="item"><b>Baby Fresh Eggs</b><span>Two farm eggs cooked to your liking, served with grilled tomato, mushrooms, toast and butter</span> <span class="price">34</span></p>
      <p class="item"><b>Healthy Time</b><span>Low fat yogurt, granola, fresh seasonal berries, honey and a glass of fresh orange juice</span> <span class="price">42</span></p>
      <p class="item"><b>Energy Time</b><span>Egg white omelette with spinach, turkey bacon, wholegrain toast and a fresh fruit smoothie</span> <span class="price">46</span></p>
      <p class="item"><b>Quaymore Time</b><span>Scrambled eggs, beef sausage, hash brown, baked beans, toast and a choice of hot drink</span> <span class="price">52</span></p>
      <p class="item"><b>The Arabic Breakfast</b><span>Foul medames, hummus, labneh, olives, fresh vegetables, zaatar bread and mint tea</span> <span class="price">48</span></p>
    </div>
  </section>

  <section class="page row-top tab-right" style="left:586px;width:106px">
    <div class="tab"></div>
    <h2 class="page-title">Sandwiches</h2>
    <div class="items compact">
      <p class="item"><b>Grilled Vegetables Sandwich</b><span>Zucchini, eggplant and peppers with pesto and mozzarella on ciabatta</span> <span class="price">38</span></p>
      <p class="item"><b>Butterfly Burger</b><span>Beef patty, cheddar, caramelised onion and pickles, served with fries</span> <span class="price">52</span></p>
      <p class="item"><b>Steak Tuna Sandwich</b><span>Seared tuna steak, rocket, tomato and wasabi mayo on toasted bread</span> <span class="price">49</span></p>
      <p class="item"><b>Beef Sirloin Steak Sandwich</b><span>Sliced sirloin, mushrooms, onions and mustard sauce on baguette</span> <span class="price">58</span></p>
      <p class="item"><b>The Traditional Club Sandwich</b><span>Chicken, turkey ham, egg, lettuce and tomato on three layers of toast</span> <span class="price">44</span></p>
      <p class="item"><b>Chicken Sandwich</b><span>Grilled chicken breast, avocado, lettuce and garlic aioli</span> <span class="price">42</span></p>
      <p class="item"><b>Steak Baguette</b><span>Tender beef strips, peppers and melted cheese in a warm baguette</span> <span class="price">55</span></p>
      <p class="item"><b>Turkey Wrap</b><span>Smoked turkey, cream cheese, cucumber and greens in a tortilla</span> <span class="price">39</span></p>
      <p class="item"><b>Beef Wrap</b><span>Spiced beef, onions, tomato and tahini sauce in a soft wrap</span> <span class="price">45</span></p>
    </div>
  </section>

  <section class="page row-top tab-left" style="left:752px;width:106px">
    <div class="tab"></div>
    <h2 class="page-title">Salads</h2>
    <div class="items">
      <p class="item"><b>Vegetarian Salad</b><span>Mixed greens, cherry tomato, cucumber, carrot, sweet corn and olives with a light lemon dressing</span> <span class="price">34</span></p>
      <p class="item"><b>Sweet Grape &amp; Goat Cheese Salad</b><span>Baby spinach, red grapes, warm goat cheese, walnuts and a balsamic honey dressing</span> <span class="price">42</span></p>
      <p class="item"><b>Beef Sirloin Salad</b><span>Grilled sirloin slices over rocket with parmesan shavings, pine nuts and mustard vinaigrette</span> <span class="price">48</span></p>
      <p class="item"><b>Tandoori Chicken Salad</b><span>Tandoori chicken, romaine, red onion, mint and a cool cucumber yogurt dressing</span> <span class="price">44</span></p>
      <p class="item"><b>Sea Food Salad</b><span>Shrimp, calamari and mussels tossed with greens, capers and citrus dressing</span> <span class="price">56</span></p>
      <p class="item"><b>Fresh Tuna Salad</b><span>Seared tuna, green beans, potato, egg and olives with a classic nicoise dressing</span> <span class="price">46</span></p>
    </div>
  </section>

  <section class="page row-top tab-right" style="left:888px;width:106px">
    <div class="tab"></div>
    <h2 class="page-title">Appetizers</h2>
    <div class="items">
      <p class="item"><b>Hummus</b><span>Chickpea puree with tahini, lemon and olive oil, served with warm bread</span> <span class="price">22</span></p>
      <p class="item"><b>Moutabal</b><span>Smoked eggplant blended with tahini, garlic and pomegranate seeds</span> <span class="price">22</span></p>
      <p class="item"><b>Warak Enab</b><span>Vine leaves stuffed with rice, tomato and herbs, cooked in lemon</span> <span class="price">26</span></p>
      <p class="item"><b>Falafel</b><span>Crispy chickpea fritters with tahini sauce and pickled turnips</span> <span class="price">24</span></p>
      <p class="item"><b>Kibbeh</b><span>Fried bulgur shells filled with spiced minced beef and pine nuts</span> <span class="price">28</span></p>
      <p class="item"><b>Sambousek</b><span>Golden pastries filled with cheese or minced meat and onion</span> <span class="price">26</span></p>
      <p class="item"><b>Cheese Rolls</b><span>Crisp rolls filled with white cheese and parsley</span> <span class="price">28</span></p>
      <p class="item"><b>Muhammara</b><span>Roasted red pepper and walnut dip with pomegranate molasses</span> <span class="price">24</span></p>
    </div>
  </section>

  <section class="page row-bottom tab-left" style="left:30px;width:100px">
    <div class="tab"></div>
    <h2 class="page-title">First Courses</h2>
    <div class="items">
      <p class="item"><b>Lentil Soup</b><span>Red lentils with cumin, lemon and crispy bread croutons</span> <span class="price">24</span></p>
      <p class="item"><b>Onion Soup</b><span>Slow cooked onions in beef broth with a gratinated cheese crouton</span> <span class="price">26</span></p>
      <p class="item"><b>Mushroom Soup</b><span>Cream of wild mushrooms with a drizzle of truffle oil</span> <span class="price">28</span></p>
      <p class="item"><b>Shrimp Cocktail</b><span>Chilled shrimp on iceberg lettuce with a classic cocktail sauce</span> <span class="price">44</span></p>
      <p class="item"><b>Beef Carpaccio</b><span>Thin sliced raw beef with rocket, parmesan and olive oil</span> <span class="price">48</span></p>
      <p class="item"><b>Smoked Salmon</b><span>Norwegian salmon with capers, red onion and toasted brioche</span> <span class="price">46</span></p>
      <p class="item"><b>Chicken Liver</b><span>Sauteed in garlic and pomegranate molasses</span> <span class="price">32</span></p>
      <p class="item"><b>Prawn Tempura</b><span>Light battered prawns with sweet chili dip</span> <span class="price">49</span></p>
    </div>
  </section>

  <section class="page row-bottom tab-right" style="left:145px;width:117px">
    <div class="tab"></div>
    <h2 class="page-title">Main Courses</h2>
    <div class="items">
      <p class="item"><b>Grilled Beef Tenderloin</b><span>Tenderloin fillet with pepper sauce, grilled vegetables and mashed potato</span> <span class="price">98</span></p>
      <p class="item"><b>Chicken Supreme</b><span>Stuffed chicken breast with mushroom cream sauce and sauteed green beans</span> <span class="price">68</span></p>
      <p class="item"><b>Grilled Fresh Salmon</b><span>Salmon fillet with lemon butter sauce, asparagus and herbed rice</span> <span class="price">86</span></p>
      <p class="item"><b>Veal Cordon Bleu</b><span>Breaded veal filled with ham and cheese, served with fries</span> <span class="price">82</span></p>
      <p class="item"><b>Thai Paella</b><span>Saffron rice with shrimp, mussels and chicken in a mild red curry</span> <span class="price">78</span></p>
      <p class="item"><b>Stuffed Calamari</b><span>Calamari tubes filled with rice and herbs in tomato sauce</span> <span class="price">74</span></p>
    </div>
  </section>

  <section class="page row-bottom tab-left" style="left:312px;width:118px">
    <div class="tab"></div>
    <h2 class="page-title">The Rotisserie</h2>
    <div class="items">
      <p class="item"><b>Spring Chicken</b><span>Whole young chicken marinated with lemon, garlic and thyme, served with fries and garlic dip</span> <span class="price">62</span></p>
      <p class="item"><b>Baby Duck</b><span>Slow roasted duck with orange glaze, braised red cabbage and potato gratin</span> <span class="price">88</span></p>
      <p class="item"><b>Boneless Lamb</b><span>Rolled lamb shoulder with rosemary jus, roasted root vegetables and oriental rice</span> <span class="price">92</span></p>
      <p class="item"><b>Beef Sirloin</b><span>Rotisserie roasted sirloin carved to order with peppercorn sauce and potato wedges</span> <span class="price">96</span></p>
      <p class="item"><b>Chicken Shawarma</b><span>Carved spiced chicken with garlic sauce, pickles and fries on a warm flatbread</span> <span class="price">58</span></p>
    </div>
  </section>

  <section class="page row-bottom tab-right" style="left:448px;width:117px">
    <div class="tab"></div>
    <h2 class="page-title">Pizza</h2>
    <div class="items compact">
      <p class="item"><b>Margherita</b><span>Tomato sauce, mozzarella and fresh basil</span> <span class="price">38</span></p>
      <p class="item"><b>Marinara</b><span>Tomato, garlic, oregano and olive oil</span> <span class="price">36</span></p>
      <p class="item"><b>Capricciosa</b><span>Mozzarella, turkey ham, mushrooms, artichoke and olives</span> <span class="price">46</span></p>
      <p class="item"><b>Tonno e Cipolla</b><span>Tuna, red onion, capers and mozzarella</span> <span class="price">44</span></p>
      <p class="item"><b>Frutti di Mare</b><span>Shrimp, calamari, mussels, garlic and parsley</span> <span class="price">58</span></p>
      <p class="item"><b>Prosciutto e Funghi</b><span>Beef prosciutto, mushrooms and mozzarella</span> <span class="price">48</span></p>
      <p class="item"><b>Calzone</b><span>Folded pizza with ricotta, ham, mushrooms and tomato</span> <span class="price">46</span></p>
      <p class="item"><b>Quattro Formaggi</b><span>Mozzarella, gorgonzola, parmesan and fontina</span> <span class="price">49</span></p>
      <p class="item"><b>Vegetariana</b><span>Grilled peppers, zucchini, eggplant and olives</span> <span class="price">40</span></p>
      <p class="item"><b>Quaymore</b><span>Chicken, sun dried tomato, rocket and pesto</span> <span class="price">54</span></p>
      <p class="item"><b>Carne</b><span>Minced beef, pepperoni, sausage and onion</span> <span class="price">52</span></p>
    </div>
  </section>

  <section class="page row-bottom tab-left" style="left:608px;width:104px">
    <div class="tab"></div>
    <h2 class="page-title">Specialties<small>and Desserts</small></h2>
    <div class="items">
      <p class="item"><b>Lobster Thermidor</b><span>Half lobster baked in a creamy mustard and cheese sauce with rice</span> <span class="price">140</span></p>
      <p class="item"><b>Beef Tenderloin "Alla Rossini"</b><span>Fillet topped with foie gras and Madeira truffle sauce</span> <span class="price">118</span></p>
      <p class="item"><b>Traditional Veal Ossobuco</b><span>Braised veal shank with gremolata and saffron risotto</span> <span class="price">104</span></p>
      <p class="item"><b>Fettuccine</b><span>Fresh ribbons with creamy wild mushroom and parmesan sauce</span> <span class="price">64</span></p>
      <div class="rule"></div>
      <div class="list">
        <p class="item">Chocolate Fondant <span class="price">32</span></p>
        <p class="item">Creme Brulee <span class="price">28</span></p>
        <p class="item">Fruit Platter <span class="price">34</span></p>
        <p class="item">Ice Cream Scoops <span class="price">24</span></p>
      </div>
    </div>
  </section>

  <section class="page row-bottom tab-right" style="left:748px;width:114px">
    <div class="tab"></div>
    <h2 class="page-title">Beverages<small>Cocktails</small></h2>
    <div class="items compact">
      <p class="item"><b>Lemon with Mint</b><span>Fresh lemon juice blended with mint leaves and ice</span> <span class="price">22</span></p>
      <p class="item"><b>Virgin Mojito</b><span>Lime, fresh mint, brown sugar and soda</span> <span class="price">26</span></p>
      <p class="item"><b>Margarita</b><span>Lime, orange and lemon juices with a salted rim</span> <span class="price">26</span></p>
      <p class="item"><b>Sea Berry</b><span>Blueberry, raspberry and strawberry with lemonade</span> <span class="price">28</span></p>
      <p class="item"><b>Blue Lemonade</b><span>Blue curacao syrup, fresh lemon and sparkling water</span> <span class="price">24</span></p>
      <p class="item"><b>Pina Colada</b><span>Pineapple juice and coconut cream blended with ice</span> <span class="price">28</span></p>
      <p class="item"><b>Passion Punch</b><span>Passion fruit, orange and a splash of grenadine</span> <span class="price">28</span></p>
      <p class="item"><b>Peach Cooler</b><span>Peach puree, iced tea and fresh lemon</span> <span class="price">26</span></p>
      <p class="item"><b>Quaymore</b><span>Mango, passion fruit, orange and strawberry layers</span> <span class="price">32</span></p>
      <p class="item"><b>Berry Splash</b><span>Mixed berries, cranberry juice and soda</span> <span class="price">28</span></p>
    </div>
  </section>

  <section class="page row-bottom tab-left" style="left:913px;width:117px">
    <div class="tab"></div>
    <h2 class="page-title">Beverages<small>Juices &amp; Milk Shakes<br>Water &amp; Soda</small></h2>
    <div class="items list">
      <p class="item">Fresh Orange <span class="price">18</span></p>
      <p class="item">Fresh Lemon <span class="price">16</span></p>
      <p class="item">Fresh Strawberry <span class="price">20</span></p>
      <p class="item">Fresh Mango <span class="price">20</span></p>
      <p class="item">Fresh Carrot <span class="price">16</span></p>
      <p class="item">Watermelon <span class="price">18</span></p>
      <p class="item">Cocktail Juice <span class="price">22</span></p>
      <div class="rule"></div>
      <p class="subhead">Milk Shake Menu</p>
      <p class="item">Vanilla <span class="price">24</span></p>
      <p class="item">Chocolate <span class="price">24</span></p>
      <p class="item">Strawberry <span class="price">24</span></p>
      <p class="item">Caramel <span class="price">26</span></p>
      <div class="rule"></div>
      <p class="item">Cola <span class="price">10</span></p>
      <p class="item">Diet Cola <span class="price">10</span></p>
      <p class="item">Lemon Soda <span class="price">10</span></p>
      <p class="item">Still Water <span class="price">8</span></p>
      <p class="item">Sparkling Water <span class="price">12</span></p>
      <p class="item">Soda <span class="price">10</span></p>
      <p class="item">Tonic <span class="price">10</span></p>
      <p class="item">Ginger Ale <span class="price">10</span></p>
    </div>
  </section>

  <section class="page row-bottom tab-left" style="left:1060px;width:115px">
    <div class="tab"></div>
    <h2 class="page-title">Beverages<small>Coffees &amp; Teas</small></h2>
    <div class="items list">
      <p class="subhead">Iced Coffee</p>
      <p class="item">Iced Latte <span class="price">22</span></p>
      <p class="item">Iced Mocha <span class="price">24</span></p>
      <p class="item">Frappe <span class="price">24</span></p>
      <p class="item">Iced Caramel <span class="price">24</span></p>
      <p class="subhead">Iced Tea</p>
      <p class="item">Peach Tea <span class="price">18</span></p>
      <p class="item">Lemon Tea <span class="price">18</span></p>
      <p class="subhead">Hot Tea</p>
      <p class="item">English Tea <span class="price">14</span></p>
      <p class="item">Green Tea <span class="price">14</span></p>
      <p class="item">Mint Tea <span class="price">14</span></p>
      <p class="item">Chamomile <span class="price">16</span></p>
      <p class="item">Earl Grey <span class="price">16</span></p>
      <p class="subhead">Coffee</p>
      <p class="item">Espresso <span class="price">14</span></p>
      <p class="item">Americano <span class="price">16</span></p>
      <p class="item">Cappuccino <span class="price">18</span></p>
      <p class="item">Latte <span class="price">18</span></p>
      <p class="item">Mocha <span class="price">20</span></p>
      <p class="item">Turkish Coffee <span class="price">14</span></p>
    </div>
  </section>

</main>
</body>
</html>
```